School and office cleaning at its best

We need a flyer for our mailing purposes to obtain new customers. Our name of the company is The Gleamwicks We have been in business since 2008 and are servicing multiple locations in san Jose CA our primary colors are black and white and red
We are servicing schools, offices, office buildings, gyms, dance studios,
We provide janitorial services weekly,biweekly and daily.
We have uniformed custodians.
We also provide carpet cleaning
Floors strip and wax
Floor steaming
Personal supervision
Quality control

Target Market(s)

Offices, schools, gyms, office buildings

Industry/Entity Type

Janitorial Service

Font styles to use
Serif

Colors

Designer to choose colors to be used in the design.

Requirements
Must have
• services provided
• Cleaning
• Carpet cleaning
• Floor strip and wax
• Floor steaming
• Janitorial services
• \Uniformed custodians
Nice to have
• surprise me
• Colors of black
• red
• white
• among others
Should not have
• Prices
• discounts

```html
<!DOCTYPE html>
<html lang="en">
<head>
<meta charset="utf-8">
<title>The Gleamwicks – Cleaning Flyer</title>
<link rel="stylesheet" href="https://fonts.googleapis.com/css2?family=Open+Sans:wght@400;600;700;800&display=swap">
<style>
:root{
  --red:#c3161c;
  --red-dark:#8e0c10;
  --ink:#1d1d1d;
  --charcoal:#2b2b2b;
  --grey:#4a4a4a;
  --paper:#f1f1f1;
  --white:#ffffff;
}
*{margin:0;padding:0;box-sizing:border-box}
html,body{width:967px;height:1200px;overflow:hidden;background:var(--paper)}
body{font-family:"Open Sans",Arial,sans-serif;color:var(--ink)}
.flyer{position:relative;width:967px;height:1200px;background:var(--paper);overflow:hidden}
.layer{position:absolute;left:0;top:0}
.brand{position:absolute;left:32px;top:44px;width:300px}
.brand-mark{display:inline-block;width:22px;height:22px;border-radius:50%;background:var(--ink);vertical-align:middle;margin-right:8px}
.brand-name{font-weight:800;font-size:40px;line-height:1.08;color:var(--ink);letter-spacing:-0.5px}
.brand-tag{margin-top:8px;font-size:13px;font-weight:700;color:var(--red);letter-spacing:0.5px}
.intro{position:absolute;left:28px;top:580px;width:600px;font-size:17px;font-weight:600;line-height:29px;color:var(--ink)}
.services-tab{position:absolute;left:0;top:688px;width:368px;height:44px;background:linear-gradient(#d3232a,var(--red-dark));border-radius:0 14px 14px 0;box-shadow:0 3px 5px rgba(0,0,0,.25);color:var(--white);font-weight:700;font-size:23px;line-height:44px;padding-left:24px}
.checklist{position:absolute;top:749px;list-style:none}
.checklist li{height:39.5px;display:flex;align-items:center;font-weight:700;font-size:17px;text-transform:uppercase}
.checklist svg{margin-right:14px;flex:none}
.checklist.col-a{left:28px}
.checklist.col-b{left:322px}
.care{position:absolute;top:878px}
.care h3{font-size:21px;font-weight:600;margin-bottom:6px}
.care ul{list-style:none}
.care li{height:25.8px;font-size:14.5px;display:flex;align-items:center}
.care li::before{content:"";width:11px;height:11px;border-radius:50%;background:var(--red);margin-right:10px;flex:none;box-shadow:inset 0 0 0 3px var(--red),inset 0 0 0 5px #f6c4c4}
.care.carpet{left:26px}
.care.floor{left:318px}
.photo-circle{position:absolute;width:224px;height:224px;border-radius:50%;background:var(--red);padding:9px;box-shadow:0 4px 8px rgba(0,0,0,.25)}
.photo-circle .ring{width:100%;height:100%;border-radius:50%;background:var(--white);padding:6px}
.photo-circle .fill{width:100%;height:100%;border-radius:50%}
.c1{left:684px;top:440px}.c1 .fill{background:radial-gradient(circle at 50% 40%,#c9ccd2,#6d727a)}
.c2{left:684px;top:676px}.c2 .fill{background:radial-gradient(circle at 50% 40%,#eef0f2,#9aa0a6)}
.c3{left:684px;top:912px}.c3 .fill{background:radial-gradient(circle at 50% 50%,#d6d8da,#5b5f63)}
.contact{position:absolute;left:112px;color:var(--white);font-weight:600;font-size:22px;display:flex;align-items:center}
.contact .icon{position:absolute;left:-30px;width:30px;height:30px;border-radius:50%;background:var(--red);display:flex;align-items:center;justify-content:center;margin-left:-16px}
.contact.phone{top:1106px}
.contact.web{top:1150px}
.social{position:absolute;top:1168px;left:712px;display:flex;gap:23px}
.social span{width:26px;height:26px;border-radius:50%;border:1.5px solid var(--white)}
</style>
</head>
<body>
<div class="flyer">

  <svg class="layer" width="967" height="620" viewBox="0 0 967 620">
    <defs>
      <linearGradient id="roomTone" x1="0" y1="0" x2="1" y2="1">
        <stop offset="0" stop-color="#e9edf1"/>
        <stop offset="0.55" stop-color="#c9d2da"/>
        <stop offset="1" stop-color="#a7afb7"/>
      </linearGradient>
      <linearGradient id="bandDark" x1="0" y1="0" x2="1" y2="0">
        <stop offset="0" stop-color="#3a3a3a"/>
        <stop offset="1" stop-color="#1c1c1c"/>
      </linearGradient>
    </defs>
    <rect role="img" aria-label="Photo of a custodian mopping a bright office floor beside a mop bucket" x="0" y="0" width="967" height="560" fill="url(#roomTone)"/>
    <path d="M0 362 C250 470 520 520 700 480 C820 452 900 410 967 398 V620 H0 Z" fill="var(--red)"/>
    <path d="M0 436 C250 520 520 545 700 510 C820 488 900 450 967 440 V620 H0 Z" fill="url(#bandDark)"/>
    <path d="M0 515 C200 555 450 565 650 545 C800 530 900 510 967 500 V620 H0 Z" fill="var(--paper)"/>
    <path d="M0 0 H470 C470 150 330 222 0 232 Z" fill="var(--white)"/>
    <path d="M470 0 C470 150 330 222 0 232" fill="none" stroke="var(--red)" stroke-width="10"/>
  </svg>

  <div class="brand">
    <div class="brand-name"><span class="brand-mark"></span>The<br>Gleamwicks</div>
    <div class="brand-tag">CLEANING PROFESSIONALS</div>
  </div>

  <p class="intro">The Gleamwicks Cleaning Professionals can provide just about any one-time or on-contract-basis janitorial service weekly, biweekly and daily that you could request!</p>

  <div class="services-tab">OUR SERVICES INCLUDE:</div>

  <ul class="checklist col-a">
    <li><svg width="20" height="18" viewBox="0 0 20 18"><rect x="1" y="3" width="14" height="14" rx="2" fill="none" stroke="#c3161c" stroke-width="2"/><path d="M4 9 L8 13 L18 2" fill="none" stroke="#c3161c" stroke-width="2.6"/></svg>General Cleaning</li>
    <li><svg width="20" height="18" viewBox="0 0 20 18"><rect x="1" y="3" width="14" height="14" rx="2" fill="none" stroke="#c3161c" stroke-width="2"/><path d="M4 9 L8 13 L18 2" fill="none" stroke="#c3161c" stroke-width="2.6"/></svg>Carpet Cleaning</li>
    <li><svg width="20" height="18" viewBox="0 0 20 18"><rect x="1" y="3" width="14" height="14" rx="2" fill="none" stroke="#c3161c" stroke-width="2"/><path d="M4 9 L8 13 L18 2" fill="none" stroke="#c3161c" stroke-width="2.6"/></svg>Floor Strip and Wax</li>
  </ul>
  <ul class="checklist col-b">
    <li><svg width="20" height="18" viewBox="0 0 20 18"><rect x="1" y="3" width="14" height="14" rx="2" fill="none" stroke="#c3161c" stroke-width="2"/><path d="M4 9 L8 13 L18 2" fill="none" stroke="#c3161c" stroke-width="2.6"/></svg>Floor Steaming</li>
    <li><svg width="20" height="18" viewBox="0 0 20 18"><rect x="1" y="3" width="14" height="14" rx="2" fill="none" stroke="#c3161c" stroke-width="2"/><path d="M4 9 L8 13 L18 2" fill="none" stroke="#c3161c" stroke-width="2.6"/></svg>Janitorial Services</li>
    <li><svg width="20" height="18" viewBox="0 0 20 18"><rect x="1" y="3" width="14" height="14" rx="2" fill="none" stroke="#c3161c" stroke-width="2"/><path d="M4 9 L8 13 L18 2" fill="none" stroke="#c3161c" stroke-width="2.6"/></svg>Uniformed Custodians</li>
  </ul>

  <div class="care carpet">
    <h3>Carpet Care</h3>
    <ul>
      <li>Carpet Vacuuming</li>
      <li>Spot Carpet Cleaning</li>
      <li>Dry, Steam &amp; Foam Shampooing</li>
      <li>Carpet Extraction</li>
      <li>Bonnet Cleaning and Deodorizing</li>
    </ul>
  </div>
  <div class="care floor">
    <h3>Floor Care</h3>
    <ul>
      <li>Marble Cleaning &amp; Polishing</li>
      <li>Tile &amp; Grout Cleaning</li>
      <li>Hardwood Floors Services</li>
      <li>Vinyl Floors</li>
      <li>Stripping, Waxing, &amp; Buffing</li>
    </ul>
  </div>

  <div class="photo-circle c1"><div class="ring"><div class="fill" role="img" aria-label="Photo of a carpet extraction machine cleaning grey carpet"></div></div></div>
  <div class="photo-circle c2"><div class="ring"><div class="fill" role="img" aria-label="Photo of a janitor cart and wet floor sign in an office"></div></div></div>
  <div class="photo-circle c3"><div class="ring"><div class="fill" role="img" aria-label="Photo of a floor buffing machine polishing a tiled floor"></div></div></div>

  <svg class="layer" width="967" height="1200" viewBox="0 0 967 1200" style="pointer-events:none">
    <defs>
      <linearGradient id="footerTone" x1="0" y1="0" x2="1" y2="0">
        <stop offset="0" stop-color="#1b1b1b"/>
        <stop offset="0.5" stop-color="#3a3a3a"/>
        <stop offset="1" stop-color="#1b1b1b"/>
      </linearGradient>
    </defs>
    <path d="M0 1075 H400 C470 1075 480 1158 570 1158 H967 V1200 H0 Z" fill="url(#footerTone)"/>
  </svg>

  <div class="contact phone">
    <span class="icon"><svg width="16" height="16" viewBox="0 0 24 24"><path d="M6.6 10.8a15 15 0 0 0 6.6 6.6l2.2-2.2a1 1 0 0 1 1-.25 11.4 11.4 0 0 0 3.6.57 1 1 0 0 1 1 1V20a1 1 0 0 1-1 1A17 17 0 0 1 3 4a1 1 0 0 1 1-1h3.5a1 1 0 0 1 1 1 11.4 11.4 0 0 0 .57 3.6 1 1 0 0 1-.25 1Z" fill="#fff"/></svg></span>
    408 555 0172
  </div>
  <div class="contact web">
    <span class="icon"><svg width="18" height="18" viewBox="0 0 24 24" fill="none" stroke="#fff" stroke-width="1.8"><circle cx="12" cy="12" r="9"/><path d="M3 12h18M12 3c3 3 3 15 0 18M12 3c-3 3-3 15 0 18"/></svg></span>
    www.thegleamwickscb.com
  </div>

  <div class="social" aria-hidden="true"><span></span><span></span><span></span><span></span></div>
</div>
</body>
</html>
```